Bayline Pet Rehoming GALA

Hi ALL!
We need an 8.5 X 11 inch, one page flyer to include all the below copy plus 8 sponsoring logos at the very bottom.
Thank YOU!

Corvel Heights Pet GALA
(Fun for Animals In Rescue!)

Sunday, August 12, 2018
1 to 4:30 p.m.

Animal Education & Adoption Event
featuring:

BK Pet Shelter & Services Rabbits & Mice

Hilltop Browsing Sheep

Thankful Hounds Haven

Featherwell Finches & Larks

Comet Pup Haven

Marla’s Feline Haven

Marvel Pup Haven

Special Guest from 1-3 p.m.
BeeBop - SF's 1st Therapy Pig!
Instagram: @BEEBOP_BKHOG
Facebook: @BEEBOP THE HOG

Activities for Kids
Dog & Cat Toy Making with Greta Vossel Canine Coaching
Animal Mask Making with Tiny Crafters
Face-in-a-Hole Photo Fun with Hugo Marsh Canine Coaching

BK PSS FREE Giveaway!
First 75 attending families receive a FREE PSS Doggie Bag containing a dog water bottle, food, shampoo, toy, treats and blinking dog collar light.

Animal Tails

1 pm Wendell’s Nook Storytime

1:30 p.m. BeeBop the Therapy Pig

1:45 pm “Tuft the Saved Hog”
Read by Author Marnie Oakhurst

2 p.m. Wendell’s Nook Singalong

2:30 p.m. Featherwell Finch Haven

2:45 p.m. Quire Pages Storytime

3 pm Browsing Sheep Refuge

3:15 p.m. The Burrow Den Puppet Show

3:45 pm BK PSS Officer Tamsin

4 p.m. Wendell’s Nook Storytime

Font styles to use
Serif

Colors

Designer to choose colors to be used in the design.

Requirements
Must have
• pig, goat, 2 dogs, kitten, dove, bunny

```html
<!DOCTYPE html>
<html lang="en">
<head>
<meta charset="utf-8">
<title>Corvel Heights Pet GALA</title>
<link rel="stylesheet" href="https://fonts.googleapis.com/css2?family=Barlow+Semi+Condensed:wght@700;800&family=Barlow:wght@700;800&family=Ubuntu:ital,wght@0,400;0,500;1,500&display=swap">
<style>
  :root {
    --page-bg: #d4d4d6;
    --red: #be1e2d;
    --red-dark: #7d0f17;
    --charcoal: #333335;
    --mint: #a9dcc3;
    --mint-light: #e6f5ee;
    --yellow: #f7e21c;
    --orange: #f5a623;
    --text: #2b2b2b;
    --rule: #555;
    --gray-a: #a4a4a4;
    --gray-b: #bcbcbc;
    --logo-text: #d6d6d6;
  }
  * { margin: 0; padding: 0; box-sizing: border-box; }
  html, body { width: 986px; height: 1200px; overflow: hidden; background: var(--page-bg); }
  .flyer {
    position: absolute; left: 29px; top: 0; width: 928px; height: 1200px;
    background: #fff; overflow: hidden;
    font-family: "Ubuntu", sans-serif; color: var(--text);
  }
  .backdrop { position: absolute; inset: 0; }
  .date {
    position: absolute; left: 0; right: 0; text-align: center; color: #fff;
    font-family: "Barlow Semi Condensed", sans-serif; font-weight: 700;
    font-size: 33px; line-height: 40px; top: 29px;
  }
  .title-top {
    position: absolute; left: 0; right: 0; top: 152px; text-align: center;
    font-family: "Barlow Semi Condensed", sans-serif; font-weight: 800;
    font-size: 70px; line-height: 80px; color: var(--charcoal); letter-spacing: -1px;
  }
  .title-main {
    position: absolute; left: 0; right: 0; top: 212px; text-align: center;
    font-family: "Barlow", sans-serif; font-weight: 800;
    font-size: 138px; line-height: 150px; letter-spacing: -2px;
    background: linear-gradient(180deg, var(--red-dark) 10%, var(--red) 60%, #9c1620 100%);
    -webkit-background-clip: text; background-clip: text; color: transparent;
  }
  .tagline {
    position: absolute; left: 0; right: 0; top: 349px; text-align: center;
    font-family: "Barlow Semi Condensed", sans-serif; font-weight: 700;
    font-size: 25px; color: var(--charcoal);
  }
  .art { position: absolute; }
  .dove-left { left: 68px; top: 34px; width: 139px; height: 186px; }
  .dove-right { left: 718px; top: 34px; width: 144px; height: 186px; }
  .animal-lineup { left: 110px; top: 373px; width: 730px; height: 280px; }

  .details { position: absolute; left: 43px; top: 668px; width: 440px; font-size: 14px; line-height: 19px; }
  .details h2 { color: var(--red); font-weight: 500; font-size: 19px; line-height: 24px; }
  .details h2.caps { font-size: 20px; }
  .partners { list-style: none; margin: 4px 0 6px; }
  .partners li { font-size: 14px; line-height: 19px; }
  .dot { display: inline-block; width: 7px; height: 7px; border-radius: 50%; background: var(--red); margin: 0 3px 1px 0; vertical-align: middle; }
  .rule { width: 290px; height: 1px; background: var(--rule); margin: 0 0 8px -6px; }
  .guest { margin-bottom: 7px; }
  .guest em { font-style: italic; font-weight: 500; }
  .guest strong { font-weight: 500; }
  .block p { margin-bottom: 7px; }

  .schedule {
    position: absolute; left: 512px; top: 650px; width: 416px; height: 409px;
    border-radius: 40px 0 0 40px;
    background: linear-gradient(135deg, var(--mint) 0%, var(--mint-light) 55%, #cdebdc 100%);
    padding: 36px 0 0 40px;
  }
  .schedule h2 { color: var(--red); font-weight: 500; font-size: 21px; line-height: 24px; margin-bottom: 7px; }
  .schedule ul { list-style: none; }
  .schedule li { position: relative; padding-left: 25px; font-size: 17px; line-height: 22.5px; margin-bottom: 5.5px; font-weight: 500; color: #333; }
  .schedule li::before { content: ""; position: absolute; left: 4px; top: 6px; width: 10px; height: 10px; border-radius: 50%; background: var(--orange); box-shadow: 0 0 0 1px #fbd46a inset; }

  .sponsors { position: absolute; left: 0; top: 1087px; width: 928px; height: 95px; display: flex; }
  .sponsors span { flex: 1; }
  .sponsors span:nth-child(odd) { background: var(--gray-a); }
  .sponsors span:nth-child(even) { background: var(--gray-b); }
  .sponsors-label {
    position: absolute; left: 0; right: 0; top: 1103px; text-align: center;
    font-weight: 500; font-size: 50px; line-height: 60px; color: var(--logo-text);
  }
</style>
</head>
<body>
<main class="flyer">
  <svg class="backdrop" viewBox="0 0 928 1200" width="928" height="1200" aria-hidden="true">
    <defs>
      <radialGradient id="mintGlow" cx="0.5" cy="0.42" r="0.65">
        <stop offset="0" stop-color="#ffffff"/>
        <stop offset="0.45" stop-color="#d9f0e5"/>
        <stop offset="1" stop-color="#a5dbc0"/>
      </radialGradient>
      <linearGradient id="sunStripe" x1="0" y1="0" x2="1" y2="0">
        <stop offset="0" stop-color="#f6a91c"/>
        <stop offset="0.5" stop-color="#f7d21c"/>
        <stop offset="1" stop-color="#f7e828"/>
      </linearGradient>
    </defs>
    <rect width="928" height="640" fill="url(#mintGlow)"/>
    <path d="M0 0 H928 V11 H770 C720 11 720 141 610 141 H318 C208 141 208 11 158 11 H0 Z" fill="#be1e2d"/>
    <path d="M0 492 C200 500 360 520 470 600 C600 560 760 510 928 500 V514 C760 524 600 574 470 614 C360 534 200 514 0 506 Z" fill="#c0202e"/>
    <path d="M0 506 C200 514 360 534 470 614 C600 574 760 524 928 514 V526 C760 536 600 586 470 626 C360 548 200 528 0 524 Z" fill="url(#sunStripe)"/>
    <path d="M0 524 C200 528 360 548 470 626 C600 586 760 536 928 526 V1200 H0 Z" fill="#ffffff"/>
  </svg>

  <div class="date">SUNDAY, AUGUST 12, 2018<br>1 TO 4:30 P.M.</div>

  <div class="art dove-left" role="img" aria-label="White dove in flight" style="background:radial-gradient(ellipse at 55% 55%, #ffffff 0%, #f1f3f2 45%, rgba(230,240,235,0) 72%);"></div>
  <div class="art dove-right" role="img" aria-label="White dove in flight" style="background:radial-gradient(ellipse at 45% 55%, #ffffff 0%, #f1f3f2 45%, rgba(230,240,235,0) 72%);"></div>

  <h1>
    <span class="title-top">CORVEL HEIGHTS</span>
    <span class="title-main">PET GALA</span>
  </h1>
  <p class="tagline">(FUN FOR ANIMALS IN RESCUE!)</p>

  <div class="art animal-lineup" role="img" aria-label="Photo of a goat, a bunny, a corgi, a golden retriever, a kitten and a pig sitting in a row" style="background:linear-gradient(90deg, rgba(60,60,60,0.75) 0%, #b89a78 16%, #d8b37a 38%, #c9a26a 52%, #a8a29c 66%, #f1c9c8 82%, rgba(241,201,200,0.4) 100%); border-radius: 60px 60px 20px 20px;"></div>

  <section class="details">
    <h2>Animal Education &amp; Adoption Event featuring:</h2>
    <ul class="partners">
      <li><i class="dot"></i>BK Pet Shelter &amp; Services Rabbits &amp; Mice</li>
      <li><i class="dot"></i>Hilltop Browsing Sheep <i class="dot"></i>Thankful Hounds Haven</li>
      <li><i class="dot"></i>Featherwell Finches &amp; Larks <i class="dot"></i>Comet Pup Haven</li>
      <li><i class="dot"></i>Marla’s Feline Haven <i class="dot"></i>Marvel Pup Haven</li>
    </ul>
    <div class="rule"></div>
    <p class="guest"><em>Special Guest from 1-3 p.m.</em><br><strong>BeeBop - SF's 1st Therapy Pig!</strong><br>Instagram: @BEEBOP_BKHOG<br>Facebook: @BEEBOP THE HOG</p>
    <div class="rule"></div>
    <div class="block">
      <h2 class="caps">ACTIVITIES FOR KIDS</h2>
      <p>Dog &amp; Cat Toy Making with Greta Vossel Canine Coaching Animal Mask Making with Tiny Crafters Face-in-a-Hole Photo Fun with Hugo Marsh Canine Coaching</p>
    </div>
    <div class="rule"></div>
    <div class="block">
      <h2 class="caps">BK PSS FREE Giveaway!</h2>
      <p>First 75 attending families receive a FREE PSS Doggie Bag containing a dog water bottle, food, shampoo, toy, treats and blinking dog collar light.</p>
    </div>
  </section>

  <section class="schedule">
    <h2>ANIMAL TAILS</h2>
    <ul>
      <li>1 pm Wendell’s Nook Storytime</li>
      <li>1:30 p.m. BeeBop the Therapy Pig</li>
      <li>1:45 pm “Tuft the Saved Hog”<br>Read by Author Marnie Oakhurst</li>
      <li>2 p.m. Wendell’s Nook Singalong</li>
      <li>2:30 p.m. Featherwell Finch Haven</li>
      <li>2:45 p.m. Quire Pages Storytime</li>
      <li>3 pm Browsing Sheep Refuge</li>
      <li>3:15 p.m. The Burrow Den Puppet Show</li>
      <li>3:45 pm BK PSS Officer Tamsin</li>
      <li>4 p.m. Wendell’s Nook Storytime</li>
    </ul>
  </section>

  <div class="sponsors" aria-hidden="true">
    <span></span><span></span><span></span><span></span><span></span><span></span><span></span><span></span>
  </div>
  <p class="sponsors-label">sponsoring logos</p>
</main>
</body>
</html>
```